Design profile for MuroDeck Nordhaven

I had a logo competition here recently, and was left with two logos that I could not choose between. Therefore, I create this competition where I want a complete design package or a visual identity for the company. I want you to create design elements that can be used both in print and online. (letterhead, envelopes, business card, website, facebook, etc.) I have also attached a picture of the car I have ordered. I'm happy if you can show how the design can be used on that as well.
What is important is that the logos are treated individually, and that the design you create reflects or builds up under the logo. I want the design to be recognizable and to have a connection with the logo and what we do. (take fizzo lumo as an example. if you remove the name, but keep the red color and the white line, then you will recognize which brand it is about right away)
You choose whether you want to make proposals only for one logo, or or both, but it is important that they are treated individually. The best overall package determines which logo I use.
I have also added an image that you can use as an example background if you want it in a facebook banner for example.
It is important that the design looks professional and unique. A number of designs have come in, but many of the designs are very similar and general. Here is a video of the printer if you need inspiration: https://clipvault.example/v/Q8ZtrMx2LwK

Industry/Entity Type

WallPrinting

Requirements
Must have
• Unique an professional design that can be used both online and print
Nice to have
• Show how to use the design on a VX Tully. (see photos attached)
Should not have
• The design can be simple, but not too simple and general. I want it to give the company an identity

```html
<!DOCTYPE html>
<html lang="en">
<head>
<meta charset="utf-8">
<title>MuroDeck Nordhaven – Stationery</title>
<link href="https://fonts.googleapis.com/css2?family=Lato:wght@400;700&display=swap" rel="stylesheet">
<style>
  :root{
    --bg:#e4e4e6;
    --paper:#ffffff;
    --ink:#111111;
    --text:#4a4a4a;
    --band:#000000;
    --accent:#0f2f6b;
    --pin:#f2c500;
    --flap:#cfcfcf;
  }
  *{box-sizing:border-box;margin:0;padding:0}
  html,body{width:1200px;height:1200px;overflow:hidden;background:var(--bg);font-family:"Lato",sans-serif}
  .canvas{position:relative;width:1200px;height:1200px}

  .letterhead{position:absolute;left:40px;top:163px;width:680px;height:874px;background:var(--paper);box-shadow:0 4px 18px rgba(0,0,0,.18)}
  .brand{position:absolute;color:var(--ink);font-weight:700;line-height:1}
  .brand .name{display:block}
  .brand .region{display:block;letter-spacing:.18em;text-transform:uppercase}
  .letterhead .brand{left:64px;top:38px}
  .letterhead .brand .name{font-size:34px}
  .letterhead .brand .region{font-size:11px;margin-top:4px;padding-left:44px}

  .contact{position:absolute;left:436px;top:26px;border-left:1px solid #333;padding-left:13px;font-size:12.5px;color:var(--ink);line-height:16px}
  .contact li{list-style:none;display:flex;align-items:center;gap:5px}
  .contact svg{width:11px;height:11px;fill:var(--ink)}

  .letter{position:absolute;left:64px;top:160px;width:550px;font-size:11px;color:var(--text)}
  .letter .date{margin-bottom:14px}
  .letter .recipient{line-height:13px;margin-bottom:42px}
  .letter .salutation{margin-bottom:22px}
  .letter p.body{text-align:justify;line-height:19.6px;margin-bottom:19.6px}
  .letter .closing{margin-top:32px}
  .signature{display:block;width:160px;height:22px;margin:10px 0 8px;background:linear-gradient(90deg,#8a8a8a22,#6a6a6a55,#8a8a8a22);border-radius:3px}
  .signer{font-size:13.5px;color:#222}
  .role{font-size:11px;margin-top:6px}

  .footer-band{position:absolute;left:0;top:804px;width:447px;height:44px;background:var(--band);color:#fff;font-size:13px;display:flex;align-items:center;padding-left:62px;gap:3px}
  .footer-band svg{width:14px;height:18px;fill:var(--pin)}
  .accent-block{position:absolute;background:var(--accent)}
  .letterhead .accent-block{left:455px;top:804px;width:225px;height:70px}

  .envelope{position:absolute;left:760px;width:400px;height:200px;background:var(--paper);box-shadow:0 3px 12px rgba(0,0,0,.16)}
  .envelope.front{top:330px}
  .envelope.back{top:570px}
  .envelope .brand{left:24px;top:20px}
  .envelope .brand .name{font-size:20px}
  .envelope .brand .region{font-size:7px;margin-top:2px;padding-left:22px}
  .envelope .footer-band{top:157px;width:255px;height:28px;font-size:8px;padding-left:24px}
  .envelope .accent-block{left:259px;top:157px;width:141px;height:43px}
  .flap{position:absolute;left:0;top:0;width:400px;height:47px}
</style>
</head>
<body>
<div class="canvas">

  <section class="letterhead">
    <div class="brand"><span class="name">MuroDeck</span><span class="region">Nordhaven</span></div>

    <ul class="contact">
      <li><svg viewBox="0 0 24 24"><path d="M6.6 10.8a15 15 0 0 0 6.6 6.6l2.2-2.2c.3-.3.7-.4 1-.2 1.1.4 2.3.6 3.6.6.6 0 1 .4 1 1V20c0 .6-.4 1-1 1A17 17 0 0 1 3 4c0-.6.4-1 1-1h3.5c.6 0 1 .4 1 1 0 1.3.2 2.5.6 3.6.1.3 0 .7-.2 1z"/></svg>047-310 882 645</li>
      <li><svg viewBox="0 0 24 24"><path d="M2 5h20v14H2zm2 2v.5l8 5 8-5V7zm0 3v7h16v-7l-8 5z"/></svg>hello@murodeck.example</li>
      <li><svg viewBox="0 0 24 24"><circle cx="12" cy="12" r="10"/></svg>www.murodeck.example</li>
    </ul>

    <div class="letter">
      <div class="date">Issuing Date: May 5, 2018</div>
      <div class="recipient">Name Of Employee Mr. XYZABC<br>Address of Employee<br>Address Line 2 etc..</div>
      <div class="salutation">Dear Mr.XYZABC</div>
      <p class="body">Lorem Ipsum has been the industry's standard dummy text ever since the 1500s, when an unknown printer took a galley of type and scrambled it to make a type specimen book. It has survived not only five centuries, but also the leap into electronic typesetting, remaining essentially unchanged. It was popularised in the 1960s with the release of Letterfold sheets containing Lorem Ipsum passages, and more recently with desktop publishing software like Pagecraft Studio including versions of Lorem Ipsum.</p>
      <p class="body">Lorem Ipsum is simply dummy text of the printing and typesetting industry. Lorem Ipsum has been the industry's standard dummy text ever since the 1500s, when an unknown printer took a galley of type and scrambled it to make a type specimen book.</p>
      <p class="body">It has survived not only five centuries, but also the leap into electronic typesetting, remaining essentially unchanged. It was popularised in the 1960s with the release of Letterfold sheets containing Lorem IpsumIpsum passages.</p>
      <div class="closing">Yours Sincerely</div>
      <span class="signature" role="img" aria-label="Handwritten signature of Elias Brandvik"></span>
      <div class="signer">Elias Brandvik</div>
      <div class="role">Managing Director</div>
    </div>

    <div class="footer-band"><svg viewBox="0 0 24 30"><path d="M12 0a11 11 0 0 0-11 11c0 8 11 19 11 19s11-11 11-19A11 11 0 0 0 12 0zm0 15a4 4 0 1 1 0-8 4 4 0 0 1 0 8z"/></svg>421, Address line goes here Country Name, 45452</div>
    <div class="accent-block"></div>
  </section>

  <section class="envelope front">
    <div class="brand"><span class="name">MuroDeck</span><span class="region">Nordhaven</span></div>
    <div class="footer-band">421, Address line goes here Country Name, 45452</div>
    <div class="accent-block"></div>
  </section>

  <section class="envelope back">
    <svg class="flap" viewBox="0 0 400 47"><polygon points="0,0 400,0 383,47 15,47" fill="var(--flap)"/></svg>
  </section>

</div>
</body>
</html>
```